Website Monitoring Business Needs a Single Page Website Design

I need a website design for a new web based service called LoopWatch. This service checks to see if a website is up or down and how quickly or slowly it is responding. Users sign up for a small monthly fee and add one or more websites to monitor based on the plan they purchase. I prefer a single page design.

There will be 3 pricing plans to start with. A free plan and then 2 paid plans. The pricing plans should be included on the single page.

Here are four close competitors to what this product will offer:

https://www.zentrovia.com/
http://haldersync.com/
https://www.brimolux.com/
https://www.quorvane5.com/

Target Market(s)

Website owners, bloggers

Industry/Entity Type

Business

Coding

Coded - Design and coding required

Number of Pages Required

1 page

Font styles to use
Sans Serif

Requirements
Must have
• Responsive design
Nice to have
• Parallax scrolling

```html
<!DOCTYPE html>
<html lang="en">
<head>
<meta charset="utf-8">
<title>LoopWatch — Website Monitoring</title>
<link rel="stylesheet" href="https://fonts.googleapis.com/css2?family=Raleway:wght@600;700&family=Noto+Sans:wght@400;700&family=Noto+Serif:wght@400&display=swap">
<style>
  :root {
    --ink: #232323;
    --white: #ffffff;
    --teal: #246f88;
    --teal-line: rgba(255,255,255,0.35);
    --footer: #262626;
    --footer-base: #1e1e1e;
    --accent: #0a9fd2;
  }
  * { box-sizing: border-box; margin: 0; padding: 0; }
  html, body { width: 1200px; height: 1137px; overflow: hidden; background: var(--white); }
  body { font-family: "Noto Sans", sans-serif; color: var(--ink); }

  .features { height: 304px; display: flex; padding: 0 22px; }
  .feature { flex: 1; text-align: center; padding-top: 66px; }
  .feature-icon { height: 66px; display: flex; justify-content: center; align-items: center; }
  .feature-title { font-family: "Raleway", sans-serif; font-weight: 700; font-size: 26px; margin-top: 10px; line-height: 30px; }
  .feature-text { font-size: 15.5px; line-height: 23.5px; margin: 12px auto 0; width: 345px; }

  .plans { height: 576px; background: var(--teal); color: var(--white); padding-top: 52px; }
  .plans-title { font-family: "Raleway", sans-serif; font-weight: 700; font-size: 31px; text-align: center; line-height: 40px; }
  .plan-grid { display: flex; margin: 26px 29px 0 28px; border: 1px solid var(--teal-line); border-radius: 3px; height: 429px; }
  .plan { flex: 1; text-align: center; padding: 0 14px; }
  .plan + .plan { border-left: 1px solid var(--teal-line); }
  .plan-name { font-family: "Raleway", sans-serif; font-weight: 700; font-size: 26px; height: 72px; line-height: 96px; border-bottom: 1px solid var(--teal-line); }
  .plan-price { font-family: "Raleway", sans-serif; font-weight: 700; font-size: 44px; height: 86px; line-height: 86px; border-bottom: 1px solid var(--teal-line); }
  .plan-features-title { font-family: "Raleway", sans-serif; font-weight: 700; font-size: 23px; margin-top: 12px; line-height: 30px; }
  .plan-features { list-style: none; font-family: "Noto Serif", serif; font-size: 15px; line-height: 28.5px; margin-top: 5px; }
  .plan-features li::before { content: "•"; margin-right: 6px; }
  .plan-button { display: inline-block; margin-top: 24px; width: 164px; height: 60px; line-height: 58px; border: 1px solid var(--teal-line); border-radius: 3px; color: var(--white); text-decoration: none; font-family: "Noto Serif", serif; font-size: 15px; }

  .site-footer { height: 212px; background: var(--footer); color: var(--white); display: flex; padding: 0 22px; }
  .footer-col { flex: 1; text-align: center; padding-top: 24px; }
  .brand { font-family: "Noto Sans", sans-serif; font-weight: 700; font-size: 28px; color: var(--accent); margin-top: 12px; line-height: 36px; }
  .footer-heading { font-family: "Raleway", sans-serif; font-weight: 700; font-size: 15.5px; line-height: 20px; }
  .call-heading { margin-top: 37px; }
  .phone { font-size: 28px; color: var(--accent); margin-top: 12px; line-height: 36px; }
  .quick-links { list-style: none; font-family: "Noto Serif", serif; font-size: 15.5px; line-height: 28.5px; margin-top: 6px; }
  .quick-links a { color: var(--white); text-decoration: none; }
  .contact-lines { font-size: 16.5px; line-height: 24px; margin-top: 8px; }

  .copyright { height: 45px; background: var(--footer-base); color: #e4e4e4; text-align: center; font-family: "Noto Serif", serif; font-size: 13px; line-height: 45px; }
</style>
</head>
<body>
  <section class="features">
    <div class="feature">
      <div class="feature-icon">
        <svg width="40" height="66" viewBox="0 0 40 66" aria-hidden="true"><path d="M6 0h20l-8 22h20L12 66l7-30H0z" fill="#232323"/></svg>
      </div>
      <h3 class="feature-title">API</h3>
      <p class="feature-text">LoopWatch provides an easy to use API For managing checks and integrating check results into your own application.</p>
    </div>
    <div class="feature">
      <div class="feature-icon">
        <svg width="32" height="52" viewBox="0 0 32 52" aria-hidden="true"><rect width="32" height="52" rx="5" fill="#232323"/><rect x="4" y="8" width="24" height="32" fill="#fff"/><circle cx="16" cy="46" r="3" fill="#fff"/><rect x="12" y="4" width="8" height="1.5" fill="#fff"/></svg>
      </div>
      <h3 class="feature-title">Mobile</h3>
      <p class="feature-text">Managing your alerts and website checks with our mobile app couldn’t be easier and you will be alerted where ever you.</p>
    </div>
    <div class="feature">
      <div class="feature-icon">
        <svg width="56" height="60" viewBox="0 0 56 60" aria-hidden="true"><circle cx="28" cy="15" r="15" fill="#232323"/><path d="M0 48c0-10 7-16 16-16h24c9 0 16 6 16 16v6a6 6 0 0 1-6 6H6a6 6 0 0 1-6-6z" fill="#232323"/></svg>
      </div>
      <h3 class="feature-title">User Friendly</h3>
      <p class="feature-text">An sint zril rationibus mei, dicta altera vel id. At vim tollit facilis voluptaria. Esse sententiae referrentur.</p>
    </div>
  </section>

  <section class="plans">
    <h2 class="plans-title">Plans</h2>
    <div class="plan-grid">
      <div class="plan">
        <h3 class="plan-name">Free</h3>
        <div class="plan-price">$0</div>
        <h4 class="plan-features-title">Features</h4>
        <ul class="plan-features"><li>Feature 1</li><li>Feature 2</li><li>Feature 3</li><li>Feature 4</li></ul>
        <a class="plan-button" href="#">LEARN MORE</a>
      </div>
      <div class="plan">
        <h3 class="plan-name">Standard</h3>
        <div class="plan-price">$30</div>
        <h4 class="plan-features-title">Features</h4>
        <ul class="plan-features"><li>Feature 1</li><li>Feature 2</li><li>Feature 3</li><li>Feature 4</li></ul>
        <a class="plan-button" href="#">LEARN MORE</a>
      </div>
      <div class="plan">
        <h3 class="plan-name">Pro</h3>
        <div class="plan-price">$50</div>
        <h4 class="plan-features-title">Features</h4>
        <ul class="plan-features"><li>Feature 1</li><li>Feature 2</li><li>Feature 3</li><li>Feature 4</li></ul>
        <a class="plan-button" href="#">LEARN MORE</a>
      </div>
    </div>
  </section>

  <footer class="site-footer">
    <div class="footer-col">
      <div class="brand">LoopWatch</div>
      <div class="footer-heading call-heading">CALL</div>
      <div class="phone">+1-555-019-2040</div>
    </div>
    <div class="footer-col">
      <div class="footer-heading">QUICK LINKS</div>
      <ul class="quick-links">
        <li><a href="#">Alerting</a></li>
        <li><a href="#">Performance</a></li>
        <li><a href="#">Monitoring</a></li>
        <li><a href="#">Pricing</a></li>
        <li><a href="#">About</a></li>
      </ul>
    </div>
    <div class="footer-col">
      <div class="footer-heading">CONTACTS</div>
      <div class="contact-lines">support@loopwatch-mail.com<br>Address &amp; Company Registration Number</div>
    </div>
  </footer>
  <div class="copyright">© 2016 LoopWatch. All Rights Reserved.</div>
</body>
</html>
```